Melbourne Locksmith Needs a Web Site

We need a web site for our new Locksmith business in Melbourne Australia. Our business is called " Corbett Row Locksmiths" . (Corbett row is a well known in the city and has the famous railway station , it is a main icon of melbourne . Maybe we could incorperate the station maybe in the front page or heading background. our services include Automotive Locksmithing ( Cuting keys to cars, opening cars etc / Master Keys Systems/ Commercial work / Domestic . Also we have no logo yet. but we can get that in the future if needed.

Target Market(s)

(Automotive ) Lost keys to cars, Trucks, Jammed Ignitions, Opening Vehicles. mobile locksmith in a van, Locked out of your house ?

Industry/Entity Type

Business

Number of Pages Required

4 page

Font styles to use
Sans Serif

Colors

Designer to choose colors to be used in the design.

Requirements
Must have
• Phone number easy to read on web site.
Nice to have
• map of where we are, show case pictures of common lock problems for automotive eg ( damaged keys/ Broken).

```html
<!DOCTYPE html>
<html lang="en">
<head>
<meta charset="utf-8">
<title>Corbett Row Locksmith</title>
<link href="https://fonts.googleapis.com/css2?family=Play:wght@400;700&family=Lato:wght@400;700&display=swap" rel="stylesheet">
<style>
:root{
  --blue:#1b5fae;
  --blue-dark:#174e92;
  --orange:#e67817;
  --ink:#222;
  --text:#444;
  --black:#0d0d0d;
  --footer:#23262d;
  --tile:#ececec;
  --white:#fff;
}
*{box-sizing:border-box;margin:0;padding:0}
html,body{width:1200px;height:3364px;overflow:hidden}
body{position:relative;font-family:'Lato',sans-serif;color:var(--text);background:var(--white)}
.abs{position:absolute}
.heading{font-family:'Play',sans-serif;font-weight:400;text-transform:uppercase;text-align:center}

/* header */
.site-header{position:absolute;left:0;top:0;width:1200px;height:135px;background:var(--white)}
.brand{position:absolute;left:0;top:0;width:430px;height:135px;background:var(--blue);display:flex;align-items:center;padding-left:78px}
.brand-name{font-family:'Play',sans-serif;font-weight:700;font-size:30px;line-height:1.2;color:var(--white);text-transform:uppercase;letter-spacing:3px}
.contact-bar{position:absolute;top:20px;left:636px;display:flex;gap:60px;font-size:19px;color:var(--ink)}
.contact-bar span{display:flex;align-items:center;gap:14px}
.contact-bar svg{width:34px;height:34px}
.nav{position:absolute;top:80px;left:530px;display:flex;gap:0}
.nav a{font-family:'Play',sans-serif;font-size:18px;color:var(--ink);text-decoration:none;text-transform:uppercase;padding:0 26px}
.nav a.active{color:var(--orange)}

/* hero */
.hero{position:absolute;left:0;top:135px;width:1200px;height:533px;background:linear-gradient(180deg,#f3c774 0%,#d99a4a 30%,#9b6a3e 60%,#5b5147 100%)}
.hero-caption{position:absolute;left:0;right:0;top:458px;text-align:center;font-family:'Play',sans-serif;font-size:27px;line-height:33px;color:var(--white);letter-spacing:1px;text-shadow:0 1px 3px rgba(0,0,0,.5)}
.hero svg.arrow{position:absolute;top:468px;width:22px;height:44px}

/* about */
.about-title{position:absolute;left:0;width:1200px;top:708px;font-size:34px;color:var(--orange)}
.about-title b{font-weight:400;color:var(--blue)}
.rule{position:absolute;height:2px;background:#ccc;width:230px;left:485px}
.about-lead{position:absolute;left:81px;width:1038px;top:790px;font-size:13.5px;line-height:20px;font-weight:700;color:var(--ink);text-align:center}
.about-body{position:absolute;left:81px;width:1038px;top:836px;font-size:13.5px;line-height:20px;text-align:center}
.btn{position:absolute;background:var(--orange);color:var(--white);font-family:'Play',sans-serif;font-weight:700;font-size:15px;text-transform:uppercase;display:flex;align-items:center;justify-content:center;border-radius:3px}

/* services */
.services{position:absolute;left:0;top:1032px;width:1200px;height:453px;background:linear-gradient(90deg,#050505 0%,#141414 55%,#2a2a2a 100%)}
.services-title{position:absolute;left:0;width:1200px;top:42px;font-size:34px;color:var(--white)}
.services-lead{position:absolute;left:81px;width:1038px;top:122px;font-size:13.5px;line-height:20px;font-weight:700;color:var(--white);text-align:center}
.service-card{position:absolute;top:202px;width:231px;height:202px}
.service-photo{position:absolute;inset:0;background:linear-gradient(160deg,#b9a58f,#6b5a4a)}
.service-label{position:absolute;left:10px;right:10px;bottom:0;height:40px;background:var(--blue);color:var(--white);font-family:'Play',sans-serif;font-size:16px;text-transform:uppercase;display:flex;align-items:center;justify-content:center}
.service-label.hot{background:var(--orange)}

/* feature */
.feature-title{position:absolute;left:81px;top:1536px;font-family:'Play',sans-serif;font-size:19px;color:var(--blue)}
.feature-body{position:absolute;left:81px;width:680px;top:1575px;font-size:13.5px;line-height:26px}
.feature-list{position:absolute;left:81px;top:1640px;width:660px;display:grid;grid-template-columns:370px 290px;row-gap:0;font-size:13.5px;list-style:none}
.feature-list li{height:38px;display:flex;align-items:center;border-bottom:1px solid #e5e5e5;padding-left:14px;position:relative}
.feature-list li::before{content:"";position:absolute;left:2px;width:5px;height:5px;border-radius:50%;background:var(--blue)}
.feature-photo{position:absolute;left:792px;top:1530px;width:325px;height:242px;border:6px solid var(--tile);background:linear-gradient(150deg,#c9231d,#7b1412 60%,#3a3f4a)}

/* inquiry + testimonial */
.inquiry{position:absolute;left:0;top:1835px;width:602px;height:415px;background:var(--blue)}
.clients{position:absolute;left:602px;top:1835px;width:598px;height:415px;background:var(--orange)}
.panel-title{position:absolute;left:0;right:0;top:50px;font-size:31px;color:var(--white)}
.field{position:absolute;background:rgba(255,255,255,.55);border-radius:3px;color:var(--white);font-size:12px;padding:10px 12px}
.avatar{position:absolute;left:238px;top:105px;width:96px;height:96px;border-radius:50%;border:4px solid var(--white);background:linear-gradient(#d7c6b8,#a08a7a)}
.quote{position:absolute;left:70px;width:460px;top:215px;font-size:12.5px;line-height:21px;color:var(--white);text-align:center}
.client-name{position:absolute;left:0;right:0;top:330px;text-align:center;font-size:14px;color:var(--white);text-transform:uppercase}
.client-role{position:absolute;left:0;right:0;top:350px;text-align:center;font-size:12px;font-style:italic;color:var(--white)}

/* gallery */
.gallery-title{position:absolute;left:0;width:1200px;top:2292px;font-size:34px;color:var(--orange)}
.gallery-title b{font-weight:400;color:var(--blue)}
.tile{position:absolute;background:var(--tile);padding:10px;border:1px solid #dcdcdc}
.tile div{width:100%;height:100%}

/* footer */
.site-footer{position:absolute;left:0;top:3040px;width:1200px;height:269px;background:var(--footer);color:#d8d8d8}
.foot-head{position:absolute;top:46px;font-family:'Play',sans-serif;font-size:16px;color:var(--white);text-transform:uppercase;padding-bottom:8px;border-bottom:2px solid #555}
.foot-links{position:absolute;left:92px;top:90px;list-style:none;font-size:13px;line-height:30px}
.foot-contact{position:absolute;left:253px;top:90px;font-size:12.5px;line-height:18px}
.foot-contact p{display:flex;gap:10px;margin-bottom:10px}
.foot-contact svg{flex:none;width:14px;height:14px;margin-top:2px}
.map{position:absolute;left:532px;top:85px;width:235px;height:143px;background:linear-gradient(135deg,#d9e4d4,#c4d4e4);border:3px solid var(--white)}
.foot-brand{position:absolute;left:825px;top:-16px;width:296px;height:285px;background:var(--orange);text-align:center}
.foot-brand-name{position:absolute;left:0;right:0;top:80px;font-family:'Play',sans-serif;font-size:25px;line-height:32px;color:var(--white);letter-spacing:3px;text-transform:uppercase}
.follow{position:absolute;left:0;right:0;top:178px;font-size:13px;color:var(--white)}
.socials{position:absolute;left:77px;top:212px;display:flex;gap:12px}
.socials span{width:28px;height:28px;background:var(--footer)}
.copyright{position:absolute;left:0;top:3309px;width:1200px;height:55px;background:var(--orange);color:var(--white);font-size:13px;padding-left:81px;display:flex;align-items:center}
</style>
</head>
<body>

<header class="site-header">
  <div class="brand"><div class="brand-name">Corbett Row<br>Locksmith</div></div>
  <div class="contact-bar">
    <span><svg viewBox="0 0 34 34"><circle cx="17" cy="17" r="15" fill="none" stroke="#e67817" stroke-width="2"/><path d="M11 10c1-1 2-1 3 0l2 3c.5 1 0 2-1 2.5 1 2 2.5 3.5 4.5 4.5.5-1 1.5-1.5 2.5-1l3 2c1 1 1 2 0 3-2 2-5 1.5-8-1s-7-6-7-10c0-1.5 0-2.5 1-3z" fill="#e67817"/></svg>123-456-7890</span>
    <span><svg viewBox="0 0 34 34"><circle cx="17" cy="17" r="15" fill="none" stroke="#e67817" stroke-width="2"/><rect x="9" y="11" width="16" height="12" rx="1" fill="#e67817"/><path d="M9 12l8 6 8-6" fill="none" stroke="#fff" stroke-width="1.5"/></svg>info@corbettrowlocksmith.au</span>
  </div>
  <nav class="nav">
    <a class="active">Home</a><a>About Us</a><a>Services</a><a>Gallery</a><a>Contact Us</a>
  </nav>
</header>

<section class="hero" role="img" aria-label="Photo of the city railway station at sunset with trams in front">
  <svg class="arrow" style="left:42px" viewBox="0 0 22 44"><path d="M20 2L2 22l18 20" fill="none" stroke="#fff" stroke-width="2"/></svg>
  <svg class="arrow" style="right:42px" viewBox="0 0 22 44"><path d="M2 2l18 20L2 42" fill="none" stroke="#fff" stroke-width="2"/></svg>
  <p class="hero-caption" style="top:458px">At Corbett Row Locksmith, We Know What It Takes To Keep Your<br>Home &amp; Business Safe &amp; Secure</p>
</section>

<h2 class="heading about-title">About Corbett Row <b>Locksmith</b></h2>
<div class="rule" style="top:760px"></div>
<p class="about-lead">Lorem ipsum dolor sit amet, consectetuer adipiscing elit, sed diam nonummy nibh euismod tincidunt ut laoreet dolore magna aliquam erat volutpat. Ut wisi enim ad minim veniam, quis nostrud exerci tation ullamcorper suscipit lobortis nisl ut aliquip ex ea commodo</p>
<p class="about-body">Lorem ipsum dolor sit amet, consectetuer adipiscing elit, sed diam nonummy nibh euismod tincidunt ut laoreet dolore magna aliquam erat volutpat. Ut wisi enim ad minim veniam, quis nostrud exerci tation ullamcorper suscipit lobortis nisl ut aliquip ex ea commodo consequat. Duis autem vel eum iriure dolor in hendrerit in vulputate velit esse molestie consequat, vel illum dolore eu feugiat nulla facilisis at vero eros et accumsan et iusto odio dignissim qui blandit praesent luptatum zzril delenit augue duis dolore te feugait nulla facilisi ex ea commodo consequat. Duis autem vel eum iriure dolor in hendrerit</p>
<div class="btn" style="left:536px;top:939px;width:126px;height:38px">Read More</div>

<section class="services">
  <h2 class="heading services-title">Our Services</h2>
  <div class="rule" style="top:100px;background:#777"></div>
  <p class="services-lead">Lorem ipsum dolor sit amet, consectetuer adipiscing elit, sed diam nonummy nibh euismod tincidunt ut laoreet dolore magna aliquam erat volutpat. Ut wisi enim ad minim veniam, quis nostrud exerci tation ullamcorper suscipit lobortis nisl ut aliquip ex ea commodo</p>
  <div class="service-card" style="left:81px"><div class="service-photo" role="img" aria-label="Photo of a key being cut on a machine"></div><div class="service-label hot">Cutting Keys to Cars</div></div>
  <div class="service-card" style="left:348px"><div class="service-photo" role="img" aria-label="Photo of a car door being opened with a tool"></div><div class="service-label">Opening Cars</div></div>
  <div class="service-card" style="left:617px"><div class="service-photo" role="img" aria-label="Photo of a hand turning a key in a lock"></div><div class="service-label">Master Keys Systems</div></div>
  <div class="service-card" style="left:886px"><div class="service-photo" role="img" aria-label="Photo of a commercial door handle lock"></div><div class="service-label">Commercial Work</div></div>
</section>

<h3 class="feature-title">consectetur adipiscing elit, sed do eiusmod Lorem ipsum dolor sit amet</h3>
<p class="feature-body">Lorem ipsum dolor sit amet, consectetur adipiscing elit, sed do eiusmod tempor incididunt ut labore et dolore magna aliqua. Ut enim ad minim veniam, quis nostrud exercitation ullamco laboris nisi ut aliquip</p>
<ul class="feature-list">
  <li>Lorem ipsum dolor sit amet, consectetur adipiscing elit,</li><li>Lorem ipsum dolor sit amet, consectetur</li>
  <li>Lorem ipsum dolor sit amet, consectetur adipiscing elit,</li><li>Lorem ipsum dolor sit amet</li>
</ul>
<div class="btn" style="left:81px;top:1738px;width:150px;height:38px">Call Us Today</div>
<div class="feature-photo" role="img" aria-label="Photo of a locksmith working inside a red car"></div>

<section class="inquiry">
  <h2 class="heading panel-title">Quick Inquiry</h2>
  <div class="field" style="left:81px;top:107px;width:215px;height:39px">Name</div>
  <div class="field" style="left:316px;top:107px;width:222px;height:39px">Phone</div>
  <div class="field" style="left:81px;top:159px;width:457px;height:38px">Email</div>
  <div class="field" style="left:81px;top:211px;width:457px;height:87px">Message</div>
  <div class="btn" style="left:265px;top:329px;width:89px;height:36px">Submit</div>
</section>

<section class="clients">
  <h2 class="heading panel-title">What Our Clients Say</h2>
  <svg class="abs" style="left:205px;top:143px" width="12" height="20" viewBox="0 0 12 20"><path d="M10 2L2 10l8 8" fill="none" stroke="#fff" stroke-width="2"/></svg>
  <svg class="abs" style="left:355px;top:143px" width="12" height="20" viewBox="0 0 12 20"><path d="M2 2l8 8-8 8" fill="none" stroke="#fff" stroke-width="2"/></svg>
  <div class="avatar" role="img" aria-label="Client portrait"></div>
  <p class="quote">Donec pulvinar libero eget enim facilisis ulte accumsan arcu lobortis. Pe impe efficitur ligula. Aliquam non augue vitae mauris pellentesque vulputate, bibendum mauris at ante Convallis sagittis. Vivamus sodales velit odio, quis feugiat lacu Fusce amet sapi dignissim feugiat ligulin erat eget ex ex sodales velit odio, quis feugiat iacdalis porta at ud.</p>
  <p class="client-name">Marcus Hale</p>
  <p class="client-role">(quis feugiat)</p>
</section>

<h2 class="heading gallery-title">Lock Problem <b>Solved Gallery</b></h2>
<div class="rule" style="top:2354px"></div>
<div class="tile" style="left:79px;top:2395px;width:506px;height:281px"><div role="img" aria-label="Photo of a locksmith working on a door lock with a tool" style="background:linear-gradient(135deg,#6d7a86,#3a3f46)"></div></div>
<div class="tile" style="left:601px;top:2395px;width:247px;height:346px"><div role="img" aria-label="Photo of two locksmiths at a doorway with a toolbox" style="background:linear-gradient(160deg,#d8c9a0,#4d4a44)"></div></div>
<div class="tile" style="left:870px;top:2395px;width:245px;height:274px"><div role="img" aria-label="Photo of hands holding a lock cylinder" style="background:linear-gradient(150deg,#b49a86,#6e5848)"></div></div>
<div class="tile" style="left:79px;top:2692px;width:242px;height:269px"><div role="img" aria-label="Photo of a hand on a door handle" style="background:linear-gradient(150deg,#c7bfb3,#8f8072)"></div></div>
<div class="tile" style="left:341px;top:2692px;width:244px;height:269px"><div role="img" aria-label="Photo of a hand holding a car key fob" style="background:linear-gradient(150deg,#d6d6d6,#8c8c8c)"></div></div>
<div class="tile" style="left:601px;top:2770px;width:247px;height:191px"><div role="img" aria-label="Photo of a car key next to a car door handle" style="background:linear-gradient(150deg,#c4c7cb,#7f858c)"></div></div>
<div class="tile" style="left:870px;top:2685px;width:245px;height:276px"><div role="img" aria-label="Photo of a locksmith fitting a lock to a wooden door" style="background:linear-gradient(150deg,#c39a62,#5b4a63)"></div></div>

<footer class="site-footer">
  <h4 class="foot-head" style="left:81px">Quick Links</h4>
  <ul class="foot-links"><li>Home</li><li>About Us</li><li>Services</li><li>Gallery</li><li>Contact</li></ul>
  <h4 class="foot-head" style="left:253px">Contact Details</h4>
  <div class="foot-contact">
    <p><svg viewBox="0 0 14 14"><path d="M7 1a4 4 0 0 0-4 4c0 3 4 8 4 8s4-5 4-8a4 4 0 0 0-4-4z" fill="#1b5fae"/><circle cx="7" cy="5" r="1.5" fill="#23262d"/></svg><span><b style="color:#fff">Corbett Row Locksmith</b><br>123 Pg Duis Aute Irur Dolore<br>Srephenderit Amit In Voluptate</span></p>
    <p><svg viewBox="0 0 14 14"><path d="M3 2c1-1 2 0 2.5 1l1 2-1.5 1.2c.8 1.6 1.8 2.6 3.3 3.3L9.5 8l2 1c1 .5 1.5 1.5.5 2.5-3 2.5-10-4.5-9-9.5z" fill="#1b5fae"/></svg><span style="color:#fff">+ (123) 456 7890</span></p>
    <p><svg viewBox="0 0 14 14"><path d="M3 2c1-1 2 0 2.5 1l1 2-1.5 1.2c.8 1.6 1.8 2.6 3.3 3.3L9.5 8l2 1c1 .5 1.5 1.5.5 2.5-3 2.5-10-4.5-9-9.5z" fill="#1b5fae"/></svg><span style="color:#fff">+ (123) 456 7890</span></p>
    <p><svg viewBox="0 0 14 14"><rect x="1" y="3" width="12" height="8" fill="#1b5fae"/><path d="M1 3l6 5 6-5" fill="none" stroke="#23262d"/></svg><span style="color:#4f8fd9">info@corbettrowlocksmith.com</span></p>
  </div>
  <h4 class="foot-head" style="left:532px">Location Map</h4>
  <div class="map" role="img" aria-label="Street map showing the shop location"></div>
  <div class="foot-brand">
    <div class="foot-brand-name">Corbett Row<br>Locksmith</div>
    <div class="follow">Follow Us:</div>
    <div class="socials"><span></span><span></span><span></span><span></span></div>
  </div>
</footer>
<div class="copyright">Copyright © 2017 Corbett Row Locksmith. All Rights Reserved</div>

</body>
</html>
```